Menu Design Project

Bo velle hair and beauty service menu
we need a menu to display a handful of our services to give our customers an idea of our pricing

Cutting
Ladies cuts from $35
Men's cuts from $25
All cuts are included with a wash and dry off

Quorvel colours
All over colours start from $55
price will vary depending upon length and thickness of hair

Foiling
starts from $50
Price will vary depending upon length of hair

Toners
from $30

Blowdries
from $35

Upstyling
wedding styling from $45
Please enquire for special occasion styling also

Beauty Services

Waxing
Eyebrow wax and shape $17.50
Lip $10
Chin/sides $20
Legs from $25
Bikini $20
XX $30
XXX $45
Back from $25
Chest from $25

Eyes
Eyebrow tinting $15
Eyelash tinting $20
Eyelash extensions from $90

Sandrift facials
Express facial $45
Deluxe facial $95

Acrylic nails
full set $60
Gel polish $35
Manicures from $35
Pedicures from $45

can provide logo and other images to help

Industry/Entity Type

Hair

Requirements
Must have
• must be called a service menu
must be eye catching and memorable but not excessive
Nice to have
• postcard style size hair menu on one side
beauty menu on the other side
elegant classy design
Should not have
• must not be called a price list
stay away from traditional price list style in terms of folding out leaflet

```html
<!DOCTYPE html>
<html lang="en">
<head>
<meta charset="utf-8">
<title>Bo velle Service Menu</title>
<link href="https://fonts.googleapis.com/css2?family=Parisienne&family=Arimo:wght@400&display=swap" rel="stylesheet">
<style>
  :root {
    --stage: #3b2416;
    --card-dark: #0e0e0e;
    --card-mid: #2a2a2a;
    --text-light: #e6e6e6;
    --text-muted: #bdbdbd;
    --hair-accent: #d8283a;
    --beauty-accent: #d9d63a;
    --white: #ffffff;
  }
  * { box-sizing: border-box; margin: 0; padding: 0; }
  html, body {
    width: 1200px; height: 750px; overflow: hidden;
    background: var(--stage);
  }
  .stage {
    position: relative; width: 1200px; height: 750px;
    display: flex; justify-content: center; align-items: center; gap: 60px;
  }
  .menu-card {
    position: relative; width: 420px; height: 600px;
    color: var(--text-light);
    font-family: "Arimo", Arial, sans-serif;
    box-shadow: 0 10px 30px rgba(0,0,0,0.5);
    overflow: hidden;
  }
  .card-pattern {
    position: absolute; inset: 0;
    background: radial-gradient(ellipse at 50% 40%, var(--card-mid) 0%, var(--card-dark) 75%);
  }
  .card-content { position: relative; padding: 34px 40px 30px 52px; }
  .card-header {
    display: flex; align-items: flex-end; gap: 28px; margin-bottom: 28px;
  }
  .brand-name {
    font-family: "Parisienne", cursive;
    font-size: 30px; color: var(--white); line-height: 1;
  }
  .menu-title { text-align: center; }
  .menu-title h1 {
    font-family: "Parisienne", cursive; font-weight: 400;
    font-size: 36px; color: var(--white); line-height: 1;
  }
  .menu-title p { font-size: 13px; color: var(--text-light); margin-top: 2px; }
  .service-group { margin-bottom: 14px; }
  .group-title {
    font-family: "Parisienne", cursive; font-weight: 400;
    font-size: 22px; line-height: 1.1;
  }
  .hair .group-title { color: var(--hair-accent); }
  .beauty .group-title { color: var(--beauty-accent); }
  .service-row {
    display: flex; justify-content: space-between;
    font-size: 12.5px; line-height: 1.3;
  }
  .service-row .price { min-width: 40px; text-align: right; }
  .service-note { font-size: 10.5px; color: var(--text-muted); line-height: 1.3; }
</style>
</head>
<body>
<main class="stage">

  <section class="menu-card hair">
    <div class="card-pattern" role="img" aria-label="Black damask pattern background"></div>
    <div class="card-content">
      <header class="card-header">
        <span class="brand-name">Bo velle</span>
        <div class="menu-title"><h1>Service Menu</h1><p>hair</p></div>
      </header>

      <div class="service-group">
        <h2 class="group-title">Cutting</h2>
        <div class="service-row"><span>Ladies cuts from</span><span class="price">35</span></div>
        <div class="service-row"><span>Men's cuts from</span><span class="price">25</span></div>
        <p class="service-note">All cuts are included with a wash and dry off</p>
      </div>

      <div class="service-group">
        <h2 class="group-title">Quorvel Colours</h2>
        <div class="service-row"><span>All over colours start from</span><span class="price">55</span></div>
        <p class="service-note">price will vary depending upon length and<br>thickness of hair</p>
      </div>

      <div class="service-group">
        <h2 class="group-title">Foiling</h2>
        <div class="service-row"><span>Starting from</span><span class="price">50</span></div>
        <p class="service-note">Price will vary depending upon length of hair</p>
      </div>

      <div class="service-group">
        <h2 class="group-title">Toners</h2>
        <div class="service-row"><span>Starting from</span><span class="price">30</span></div>
      </div>

      <div class="service-group">
        <h2 class="group-title">Blowdries</h2>
        <div class="service-row"><span>Starting from</span><span class="price">35</span></div>
        <p class="service-note">price will vary depending upon length and<br>thickness of hair</p>
      </div>

      <div class="service-group">
        <h2 class="group-title">Upstyling</h2>
        <div class="service-row"><span>wedding styling from</span><span class="price">45</span></div>
        <p class="service-note">Please enquire for special occasion styling also</p>
      </div>
    </div>
  </section>

  <section class="menu-card beauty">
    <div class="card-pattern" role="img" aria-label="Black damask pattern background"></div>
    <div class="card-content">
      <header class="card-header">
        <span class="brand-name">Bo velle</span>
        <div class="menu-title"><h1>Service Menu</h1><p>beauty</p></div>
      </header>

      <div class="service-group">
        <h2 class="group-title">Waxing</h2>
        <div class="service-row"><span>Eyebrow wax and shape</span><span class="price">17.50</span></div>
        <div class="service-row"><span>Lip</span><span class="price">10</span></div>
        <div class="service-row"><span>Chin/sides</span><span class="price">20</span></div>
        <div class="service-row"><span>Legs from</span><span class="price">25</span></div>
        <div class="service-row"><span>Bikini</span><span class="price">20</span></div>
        <div class="service-row"><span>XX</span><span class="price">30</span></div>
        <div class="service-row"><span>XXX</span><span class="price">45</span></div>
        <div class="service-row"><span>Back starting from</span><span class="price">25</span></div>
        <div class="service-row"><span>Chest starting from</span><span class="price">25</span></div>
      </div>

      <div class="service-group">
        <h2 class="group-title">Eyes</h2>
        <div class="service-row"><span>Eyebrow tinting</span><span class="price">15</span></div>
        <div class="service-row"><span>Eyelash tinting</span><span class="price">20</span></div>
        <div class="service-row"><span>Eyelash extensions from</span><span class="price">90</span></div>
      </div>

      <div class="service-group">
        <h2 class="group-title">Sandrift Facials</h2>
        <div class="service-row"><span>Express facial</span><span class="price">45</span></div>
        <div class="service-row"><span>Deluxe facial</span><span class="price">95</span></div>
      </div>

      <div class="service-group">
        <h2 class="group-title">Nails</h2>
        <div class="service-row"><span>Acrylic full set</span><span class="price">60</span></div>
        <div class="service-row"><span>Gel polish</span><span class="price">35</span></div>
        <div class="service-row"><span>Manicures from</span><span class="price">35</span></div>
        <div class="service-row"><span>Pedicures from</span><span class="price">45</span></div>
      </div>
    </div>
  </section>

</main>
</body>
</html>
```